Poster / Flyer / Advertisement for Frosk Brew Chill (Unique Product!)

We’re selling alcoholic (7.5%) flavored ice for beer…for example, you might try our Lime flavor in a Valdor. We need a great ad/poster…please follow these guidelines:
USE THE PRODUCT PHOTO & KEEP IT SIMPLE!
Use the attached “action shot” of our product prominently. I prefer just the glass of beer, so turn off the layer with the beer bottle. Photoshop in a great background and KEEP IT SIMPLE - the product shot pretty much says it all. Find a great background, add the words “Your beer is getting warm”, and layer in some of our branding (see below). That’s it! Don’t make the poster too busy!
USE OUR CURRENT BRANDING
I’ve attached AI files with all of our branding. Layer in the pattern used on the packaging, our logo, and probably the “Frosk Chill” banner. Also, given that our most popular flavor is Lime in a Valdor, I would look for a background that helps express that (just a thought, it’s up to you to make it look good!).
MAKE IT VERSATILE
We need this to be versatile and easily scale up or down in size for various applications such as:
1) Large format poster for the front window of a convenience store
2) Smaller format for poster ads in bars/restaurants
3) Even smaller format for window clings that go on the glass doors of beer coolers
I also want the words for the poster to be easily changeable for the different applications:
1) Bar – I would use the tagline “Your beer is getting warm”
2) Convenience Store – I would use the line “Don’t drink warm beer…check the freezer!” or something similar. Just need it easy to change
Updates
Project Deadline Extended
Reason: Still deciding on designs. Need time to review with business partners. Thanks all!
Target Market(s)
Beer drinkers - especially those that like fruity beers like summer shandy
Industry/Entity Type
Brewery
Font styles to use
Other font styles liked:
- Use attached fonts!
Colors
Designer to choose colors to be used in the design.
Requirements
Must have
- Use the product shot and our branding...and a simple design!
Nice to have
- Want a "drinking an ice cold beer on a summer day" feel to this.

```html
<!DOCTYPE html>
<html lang="en">
<head>
<meta charset="utf-8">
<title>Frosk Brew Chill – Your Beer Is Getting Warm</title>
<link rel="stylesheet" href="https://fonts.googleapis.com/css2?family=Montserrat:wght@800&family=Raleway:wght@300&family=Roboto+Slab:wght@700&display=swap">
<style>
  :root {
    --bg-light: #a7bcb3;
    --bg-mid: #5f7f72;
    --bg-dark: #15301f;
    --headline-yellow: #f7e47c;
    --headline-lime: #80f52a;
    --headline-shadow: #23231a;
    --brand-dark: #2a2626;
    --brand-lime: #8ee03a;
    --beer-light: #f8e08c;
    --beer-deep: #e3ad34;
    --lime-light: #8fdc4a;
    --lime-deep: #3f8f1c;
    --band-white: #ffffff;
    --band-ink: #111111;
    --stripe-lime: #9ad94a;
    --stripe-ink: #1f3a12;
    --wood-light: #4a2a1e;
    --wood-dark: #1a0f0b;
  }
  html, body {
    margin: 0;
    padding: 0;
    width: 800px;
    height: 1200px;
    overflow: hidden;
  }
  .poster {
    position: relative;
    width: 800px;
    height: 1200px;
    overflow: hidden;
    background:
      radial-gradient(ellipse 520px 700px at 140px 520px, var(--bg-light) 0%, var(--bg-mid) 55%, transparent 100%),
      linear-gradient(100deg, var(--bg-mid) 0%, #3c5e4a 45%, var(--bg-dark) 100%);
  }
  .droplet-backdrop {
    position: absolute;
    inset: 0;
  }
  .brand-mark {
    position: absolute;
    left: 52px;
    top: 108px;
    display: flex;
    align-items: center;
    gap: 14px;
  }
  .brand-mark__dot {
    width: 56px;
    height: 56px;
    border-radius: 50%;
    background: var(--brand-dark);
  }
  .brand-mark__name {
    font-family: "Montserrat", sans-serif;
    font-weight: 800;
    font-size: 26px;
    color: var(--brand-lime);
    white-space: nowrap;
  }
  .headline {
    position: absolute;
    left: 22px;
    top: 330px;
    margin: 0;
    font-family: "Montserrat", sans-serif;
    font-weight: 800;
    text-transform: uppercase;
    line-height: 1;
  }
  .headline__line {
    display: block;
    font-size: 76px;
    line-height: 86px;
    letter-spacing: -1px;
    color: var(--headline-yellow);
    text-shadow: 3px 3px 0 var(--headline-shadow);
  }
  .headline__accent {
    display: block;
    font-size: 106px;
    line-height: 110px;
    letter-spacing: -2px;
    color: var(--headline-lime);
    text-shadow: 4px 4px 0 var(--headline-shadow);
  }
  .product-glass {
    position: absolute;
    left: 424px;
    top: 100px;
    width: 344px;
    height: 708px;
    border-radius: 18px 18px 30px 30px;
    background:
      linear-gradient(180deg, rgba(255,255,255,0.85) 0%, rgba(255,250,220,0.9) 14%, transparent 28%),
      linear-gradient(90deg, var(--beer-deep) 0%, var(--beer-light) 40%, var(--beer-light) 60%, var(--beer-deep) 100%);
  }
  .product-lime {
    position: absolute;
    left: 292px;
    top: 740px;
    width: 288px;
    height: 208px;
    border-radius: 50%;
    background: radial-gradient(ellipse at 40% 35%, var(--lime-light) 0%, var(--lime-deep) 100%);
  }
  .banner {
    position: absolute;
    inset: 0;
  }
  .banner__title {
    font-family: "Raleway", sans-serif;
    font-weight: 300;
    font-size: 82px;
    letter-spacing: 4px;
    fill: var(--band-ink);
  }
  .banner__warning {
    font-family: "Roboto Slab", serif;
    font-weight: 700;
    font-size: 12px;
    letter-spacing: 0.5px;
    fill: var(--stripe-ink);
  }
</style>
</head>
<body>
  <main class="poster">
    <div class="droplet-backdrop" role="img" aria-label="Misty green glass backdrop covered in cold water droplets"></div>

    <div class="brand-mark">
      <span class="brand-mark__dot"></span>
      <span class="brand-mark__name">Frosk Brew Chill</span>
    </div>

    <h1 class="headline">
      <span class="headline__line">Your</span>
      <span class="headline__line">Beer is</span>
      <span class="headline__line">Getting</span>
      <span class="headline__accent">Warm</span>
    </h1>

    <div class="product-glass" role="img" aria-label="Pint glass of golden beer splashing as a lime flavoured ice cube drops in"></div>
    <div class="product-lime" role="img" aria-label="Whole fresh lime labelled with the lime flavour"></div>

    <svg class="banner" width="800" height="1200" viewBox="0 0 800 1200" aria-hidden="false">
      <polygon points="0,1108 800,884 800,1200 0,1200" fill="url(#woodTone)" role="img" aria-label="Dark wooden bar top with lime slice packaging pattern"/>
      <defs>
        <linearGradient id="woodTone" x1="0" y1="0" x2="1" y2="1">
          <stop offset="0" stop-color="#3a2017"/>
          <stop offset="0.5" stop-color="#4a2a1e"/>
          <stop offset="1" stop-color="#1a0f0b"/>
        </linearGradient>
      </defs>
      <polygon points="0,1004 800,780 800,852 0,1090" fill="var(--band-white)"/>
      <polygon points="0,1090 800,852 800,870 0,1108" fill="var(--stripe-lime)"/>
      <g transform="rotate(-16.5 400 980)">
        <text class="banner__title" x="430" y="972" text-anchor="middle">FROSK CHILL</text>
      </g>
      <g transform="rotate(-16.5 0 1099)">
        <text class="banner__warning" x="0" y="1103">CONTAINS ALCOHOL    CONTAINS ALCOHOL    CONTAINS ALCOHOL    CONTAINS ALCOHOL    CONTAINS ALCOHOL    CONTAINS ALCOHOL</text>
      </g>
    </svg>
  </main>
</body>
</html>
```